Modern card design needed for building development company

We are looking for a sharp modern new look for our business cards.
We are a New Zealand based company called TKV Ventures NZ LTD that specialises in subdividing large sections, housing and commercial buildings.
We have attached a photo of the current logo and would like to see it improved somehow as it looks a bit dated.
We are open to any colours.

Target Market(s)

Investors, Property buyers

Industry/Entity Type

Investment

Contact Information for Business Card

TKV VENTURES NZ LTD
www.tkvventuresnz.co.nz

Howard Pennick
Phone +64 21 843 192
Email hdpennick@fernmail.co.nz

Font styles to use
Serif
Sans Serif

Colors
0792cd
33a6d7
85cae6
6b449b
886aae
f04a50
ec1f27
f37122
f68d4d

Requirements
Must have
• Please try and make the logo more modern or if you have a similar one we would like to see it.

```html
<!DOCTYPE html>
<html lang="en">
<head>
<meta charset="utf-8">
<title>TKV Ventures NZ LTD – Business Card</title>
<link rel="stylesheet" href="https://fonts.googleapis.com/css2?family=Open+Sans:ital,wght@0,400;0,700;1,400&family=Noto+Sans:wght@400&display=swap">
<style>
  :root {
    --canvas: #a4a1a2;
    --coral: #f04a50;
    --card-white: #ffffff;
    --brand-dark: #8e1b22;
    --text-dark: #333333;
    --text-grey: #555555;
    --skyline: #f1f1f1;
  }
  * { margin: 0; padding: 0; box-sizing: border-box; }
  html, body { width: 1200px; height: 1200px; overflow: hidden; }
  body { background: var(--canvas); position: relative; font-family: "Noto Sans", sans-serif; }

  .card { position: absolute; border-radius: 22px; overflow: hidden; }

  /* Front */
  .card-front { left: 212px; top: 106px; width: 787px; height: 432px; background: var(--coral); }
  .front-brand {
    position: absolute; left: 0; right: 0; top: 196px;
    display: flex; align-items: center; justify-content: center; gap: 16px;
    color: #fff; font-family: "Open Sans", sans-serif; font-weight: 700;
    font-size: 36px; letter-spacing: 2px;
  }
  .brand-square { width: 22px; height: 22px; background: #fff; }
  .front-url {
    position: absolute; left: 0; right: 0; top: 392px;
    display: flex; align-items: center; justify-content: center; gap: 8px;
    color: #fff; font-family: "Open Sans", sans-serif; font-style: italic;
    font-size: 15px; letter-spacing: 3px;
  }
  .front-url .rule { width: 32px; height: 1px; background: rgba(255,255,255,0.8); }

  /* Back */
  .card-back { left: 210px; top: 634px; width: 794px; height: 438px; background: var(--card-white); }
  .skyline {
    position: absolute; left: 80px; top: 20px; width: 714px; height: 418px;
    background: linear-gradient(180deg, rgba(241,241,241,0) 0%, var(--skyline) 35%, #ececec 100%);
  }
  .name-bar { position: absolute; left: 0; top: 62px; width: 13px; height: 44px; background: var(--coral); }
  .holder-name {
    position: absolute; left: 30px; top: 55px;
    font-family: "Open Sans", sans-serif; font-weight: 700; font-size: 26px;
    color: var(--coral); letter-spacing: 0.5px;
  }
  .holder-title { position: absolute; left: 32px; top: 89px; font-size: 17px; color: var(--text-grey); }

  .address { position: absolute; left: 29px; top: 278px; font-size: 17px; line-height: 20px; color: var(--text-dark); letter-spacing: 0.6px; }
  .contact-list { position: absolute; left: 29px; top: 336px; list-style: none; }
  .contact-list li {
    display: flex; align-items: center; gap: 7px; height: 28.5px;
    font-size: 17px; color: var(--text-dark); letter-spacing: 0.6px;
  }
  .contact-list svg { width: 19px; height: 19px; flex: none; }

  .back-brand {
    position: absolute; left: 476px; top: 390px;
    font-family: "Open Sans", sans-serif; font-weight: 700; font-size: 22px;
    color: var(--brand-dark); letter-spacing: 1.8px;
  }
</style>
</head>
<body>

<section class="card card-front">
  <div class="front-brand"><span class="brand-square"></span>TKV VENTURES NZ LTD</div>
  <div class="front-url"><span class="rule"></span>www.tkvventuresnz.co.nz<span class="rule"></span></div>
</section>

<section class="card card-back">
  <div class="skyline" role="img" aria-label="Faint city skyline illustration in light grey"></div>

  <div class="name-bar"></div>
  <h1 class="holder-name">Howard Pennick</h1>
  <p class="holder-title">Title</p>

  <p class="address">PO BOX 48215<br>Devonport, Auckland, New Zealand</p>

  <ul class="contact-list">
    <li>
      <svg viewBox="0 0 20 20"><circle cx="10" cy="10" r="8.5" fill="none" stroke="#f04a50" stroke-width="1.5"/><path d="M7 5.5c.6-.3 1 .1 1.3.8l.5 1.2c.2.5 0 .8-.4 1.1-.3.3-.2.7.2 1.3.5.7.9 1.1 1.5 1.3.4.1.7-.1 1-.5.3-.3.6-.4 1.1-.1l1.1.7c.6.4.7.8.3 1.3-.8 1-2 1.2-3.4.4-1.7-1-3.2-3-3.5-4.8-.2-1.3.1-2.3.3-2.7z" fill="#f04a50"/></svg>
      64 21 843 192
    </li>
    <li>
      <svg viewBox="0 0 20 20"><rect x="2" y="5" width="16" height="10.5" fill="#f04a50"/><path d="M2 5l8 6 8-6" fill="none" stroke="#fff" stroke-width="1.3"/></svg>
      hdpennick@fernmail.co.nz
    </li>
    <li>
      <svg viewBox="0 0 20 20" fill="none" stroke="#f04a50" stroke-width="1.4"><circle cx="10" cy="10" r="8"/><ellipse cx="10" cy="10" rx="3.5" ry="8"/><path d="M2 10h16M3.5 6h13M3.5 14h13"/></svg>
      www.tkvventuresnz.co.nz
    </li>
  </ul>

  <div class="back-brand">TKV VENTURES NZ LTD</div>
</section>

</body>
</html>
```